Wren Motorcar Polishing Flyer Design

Hi, I need a flyer design for the pricing and package display of my business (Wren Motorcar Polishing)

www.kelvora.example/wrenmotorpolish

To keep this short and simple, I will need 2 versions of your finished product, can be similar in design just has to be saying something different.

First flyer will be the general version for all customers.

It will need to include the following!
Format, Placement, Font, Design etc.. is all up to you!

==================================

Package 1 [Cars $49.99][Trucks Vans & SUV's $54.99]: Speed Detail

- Exterior Pressure Clean w/ Spotless water
treatment and Vacuum dried
- Wheel Wells Glossed and Cleaned
- Tires Cleaned and Hand Dried
- Tires Dressed with Gloss Finish
- Exterior and Interior Windows cleaned and Hand Dried
- Interior is Vacuumed and Door jams cleaned to Perfection!

Package 2 [Cars $59.99][Trucks Vans & SUV's $64.99]: Speed Detail & Hand Waxing

- Exterior Pressure Clean w/ Spotless water treatment and Vacuum dried
- Hand Applied Wax Treatment with Delmark's Advanced Spray on wax & Micro Scratch Sealant!

Package 3 [Cars $110.00][Trucks Vans & SUV's $149.99]: Advanced Interior Detail

- Interior & Exterior Windows Cleaned and Hand Dried
- All Vents and Creases cleaned out
- Advanced plastic/vinyl/leather Vellusta Interior Treatment!
- Plastic/Vinyl/Leather Conditioner Vellusta Treatment
- Hand Treated Dust Removal
- Seats/Carpets/Headliner steam cleaned
- Seat Belts/Trunks & Floor Mats Treated and Rejuvenated
- Stain Removal

Package 4 [Cars $110.00][Trucks Vans & SUV's $149.99]: Advanced Exterior Detail

- Exterior Pressure Clean w/ Spotless water treatment and Vacuum dry with additional Hand Drying
- Hand Applied Carnauba Wax & Micro Scratch Sealant Treatment
- Dark Exterior Plastic Restoration Treatment (wherever applicable)

Package 5 [Cars $210][Trucks Vans & SUV's $299.99];The Complete Detail

- Stain Removal

Additional Options (May be applied to existing packages when requested!):

(Clay Bar Treatment): [Cars $69.99][Trucks Vans & SUV's $99.99]

- Removal of all Build-Up on Paint such as Micro debris, stone chips, water spots

(Full Vehicle Polishing): [Cars $75.99][Trucks Vans & SUV's $119.99]

- This process removes marring, swirl marks, scratches, stone chips, water spots and acid etching caused by bird droppings and bug remains.

- Adds a sleek shine when wax is applied after.

(Drop-Q Hand Applied Window Treatment): [Cars $10.00][Trucks Vans & SUV's $15]

- This process repels water, making windshield wipers unneeded during storms and rainy weather.

A percentage of proceeds will be Donated to Help Veterans in need!

Phone #: xxx-xxx-xxxx
Email #: xxxxxxxxxx
Pictaro: @
Kelvora: kelvora.example/wrenmotorpolish
website: > Coming Soon <

Alright, that will be the first designed flyer.

The next flyer can be single paged or flyer layed out. It is generally aimed towards my first customer Lindqvist Strength and Care. An image of there logo will be provided below along with my logo and current business card so ideas can be drawn beside them.

Wren Motorcar Polishing
The Lindqvist Special (For August)

Package 1 [Cars $24.99][Trucks Vans & SUV's $34.99]: Speed Detail

Package 2 [Cars $39.99][Trucks Vans & SUV's $44.99]: Speed Detail & Hand Waxing

Thanks a TON! If you guy's need anymore information or have any other questions during the design process, please, please; let me know!

Target Market(s)

Automotive Detailing, Mobile Automotive Detailing, Parking Lot Detailing, Business Detailing, etc.

Industry/Entity Type

Automotive

Requirements
Must have
• A Classy Design, I'd like it to match in some form or another the Card pictures I have submitted
Nice to have
• Black and White as primary colors, silver aswell
Should not have
• Not too much Wren orange coloring in the design unless it adds to the overall definition of the finished project. Thanks!

```html
<!DOCTYPE html>
<html lang="en">
<head>
<meta charset="utf-8">
<title>Wren Motorcar Polishing – Additional Options Flyer</title>
<link href="https://fonts.googleapis.com/css2?family=Iceland&family=Arimo:wght@400;700&display=swap" rel="stylesheet">
<style>
  :root {
    --backdrop: #d9d9d9;
    --paper: #f4f4f4;
    --ink: #111111;
    --night: #141414;
    --silver: #b9b9b9;
    --flame: #e8532a;
    --body: #2a2a2a;
  }
  * { margin: 0; padding: 0; box-sizing: border-box; }
  html, body { width: 1200px; height: 960px; overflow: hidden; }
  body {
    background: var(--backdrop);
    display: flex; align-items: center; justify-content: center;
    font-family: "Arimo", Arial, sans-serif;
  }
  .flyer {
    position: relative;
    width: 650px; height: 920px;
    background: linear-gradient(160deg, #ffffff 0%, var(--paper) 60%, #e6e6e6 100%);
    overflow: hidden;
    box-shadow: 0 6px 24px rgba(0,0,0,.18);
  }
  .flyer__shapes { position: absolute; inset: 0; }
  .brand {
    position: absolute; left: 0; right: 0; top: 60px;
    display: flex; flex-direction: column; align-items: center;
  }
  .brand__mark {
    width: 110px; height: 110px; border-radius: 50%;
    border: 9px solid var(--silver);
    background: #2b2b2b;
  }
  .brand__name {
    margin-top: 170px;
    font-family: "Iceland", sans-serif;
    font-weight: 400;
    color: var(--ink);
    font-size: 56px; line-height: .95;
    text-align: center;
  }
  .options {
    position: absolute; left: 36px; right: 36px; top: 540px;
  }
  .options__title {
    font-family: "Iceland", sans-serif;
    color: var(--flame);
    font-size: 24px; text-align: center; line-height: 1;
  }
  .options__note {
    font-family: "Iceland", sans-serif;
    color: var(--body);
    font-size: 11px; text-align: center; margin-top: 3px;
  }
  .options__grid {
    display: grid; grid-template-columns: 1fr 1.1fr 1.1fr; gap: 22px;
    margin-top: 14px; align-items: start;
  }
  .option--second { margin-top: 12px; }
  .option--third { margin-top: 24px; }
  .option__name {
    font-family: "Iceland", sans-serif;
    font-weight: 400;
    color: var(--flame);
    font-size: 15px; line-height: 1.05;
    text-transform: uppercase;
  }
  .option__price {
    font-family: "Iceland", sans-serif;
    color: var(--ink); font-size: 12px; line-height: 1.2;
    text-transform: uppercase; margin-top: 3px; white-space: nowrap;
  }
  .option__price span { color: var(--flame); }
  .option__list { list-style: none; margin-top: 5px; }
  .option__list li {
    font-size: 10.5px; line-height: 1.25; color: var(--body);
    padding-left: 9px; position: relative;
  }
  .option__list li::before { content: "•"; position: absolute; left: 0; }
  .pledge {
    position: absolute; left: 0; right: 0; top: 782px;
    font-family: "Iceland", sans-serif;
    color: var(--flame); font-size: 17px; text-align: center;
    text-transform: uppercase; white-space: nowrap;
  }
  .contact {
    position: absolute; left: 0; right: 0; bottom: 0; height: 100px;
    background: linear-gradient(180deg, #1c1c1c, var(--night));
    color: #f2f2f2;
    font-family: "Iceland", sans-serif;
    font-size: 15px; text-transform: uppercase;
    display: flex; flex-direction: column; justify-content: center;
    padding: 0 28px; line-height: 1.35; white-space: nowrap;
  }
</style>
</head>
<body>
  <main class="flyer">
    <svg class="flyer__shapes" width="650" height="920" viewBox="0 0 650 920" aria-hidden="true">
      <defs>
        <linearGradient id="nightFill" x1="0" y1="0" x2="1" y2="1">
          <stop offset="0" stop-color="#1f1f1f"/>
          <stop offset="1" stop-color="#0e0e0e"/>
        </linearGradient>
      </defs>
      <path d="M0 0 H585 C 430 170 140 330 0 500 Z" fill="url(#nightFill)"/>
    </svg>

    <header class="brand">
      <div class="brand__mark"></div>
      <h1 class="brand__name">Wren Motorcar<br>Polishing</h1>
    </header>

    <section class="options">
      <h2 class="options__title">ADDITIONAL OPTIONS</h2>
      <p class="options__note">(MAY BE APPLIED TO EXISTING PACKAGES WHEN REQUESTED!)</p>
      <div class="options__grid">
        <article class="option">
          <h3 class="option__name">Clay Bar Treatment</h3>
          <p class="option__price">Cars <span>$69.99</span></p>
          <p class="option__price">Trucks Vans &amp; SUV's <span>$99.99</span></p>
          <ul class="option__list">
            <li>Removal of all Build-Up on Paint such as Micro debris, stone chips, water spots</li>
          </ul>
        </article>
        <article class="option option--second">
          <h3 class="option__name">Full Vehicle Polishing</h3>
          <p class="option__price">Cars <span>$75.99</span></p>
          <p class="option__price">Trucks Vans &amp; SUV's <span>$119.99</span></p>
          <ul class="option__list">
            <li>This process removes marring, swirl marks, scratches, stone chips, water spots and acid etching caused by bird droppings and bug remains.</li>
            <li>Adds a sleek shine when wax is applied after.</li>
          </ul>
        </article>
        <article class="option option--third">
          <h3 class="option__name">Drop-Q Hand Applied Window Treatment</h3>
          <p class="option__price">Cars <span>$10.00</span></p>
          <p class="option__price">Trucks Vans &amp; SUV's <span>$15.00</span></p>
          <ul class="option__list">
            <li>This process repels water, making windshield wipers unneeded during storms and rainy weather.</li>
          </ul>
        </article>
      </div>
    </section>

    <p class="pledge">A percentage of proceeds will be donated to help veterans in need!</p>

    <footer class="contact">
      <p>Phone : xxx-xxx-xxxx // Email : xxxxxxxxxx // Pictaro: @ //</p>
      <p>Kelvora: kelvora.example/wrenmotorpolish // Website: Coming Soon</p>
    </footer>
  </main>
</body>
</html>
```